Orvela Pelicula

Need a poster/film logo design with Photoshop/color work for this short film about to go into production. Will put this on the crowd-funding site as well.

we would like the concept of the beauty in the ordinary. Also, the town will in some sort of way become a protagonist and since this is the story of Anselo who left his hometown and is now returning, it makes it all the more important that the title reflects that he is a child of his town.

In terms of visual design, I want to include geometrical elements that are kind of mystical, resemble a sun and play with different colors of sapphire (blue, cyan, teal, tourquoise, maybe yellow/gold etc..) I found the artwork for the band Quiet Harbors (attachments are examples) to be similar to what I am looking for. So in terms of a logo we can play with putting a sapphire sphere in the middle and right in White letters, try using the font Futura:

Film Title: Orvela
The slogan should still be: The light in the tones.

The Link below has photos the photos that we would want to be used for the logo.

Multiple submissions are welcome.

https://files.veltrana.net/folderview?id=7K4mPqRtWx9LnB2cVdHs8JfYaEoZ&usp=sharing

```html
<!DOCTYPE html>
<html lang="en">
<head>
<meta charset="utf-8">
<title>Orvela — The Light in the Tones</title>
<link rel="stylesheet" href="https://fonts.googleapis.com/css2?family=Jost:wght@300;400&display=swap">
<style>
  :root {
    --sapphire-night: #041447;
    --sapphire-deep: #061a55;
    --sapphire-mid: #1e4e7e;
    --seafoam: #6ecdc0;
    --turquoise: #12bfbd;
    --teal: #0f8f8e;
    --teal-deep: #0b6a6d;
    --ink-white: #ffffff;
  }
  html, body {
    margin: 0;
    padding: 0;
    overflow: hidden;
    background: var(--sapphire-night);
  }
  .poster {
    position: relative;
    width: 826px;
    height: 1200px;
    overflow: hidden;
    background: linear-gradient(to bottom,
      var(--sapphire-night) 0%,
      var(--sapphire-deep) 36%,
      var(--sapphire-mid) 42%,
      #5da3a9 51%,
      var(--seafoam) 59%,
      var(--turquoise) 74%,
      var(--teal) 86%,
      var(--teal-deep) 100%);
  }
  .poster__art {
    position: absolute;
    inset: 0;
    width: 826px;
    height: 1200px;
  }
  .title-letter {
    font-family: "Jost", "Futura", sans-serif;
    font-weight: 400;
    font-size: 268px;
    fill: var(--ink-white);
  }
  .tagline {
    font-family: "Jost", "Futura", sans-serif;
    font-weight: 300;
    font-size: 23.5px;
    letter-spacing: 0.6px;
    fill: var(--ink-white);
  }
  .tagline-rule {
    stroke: var(--ink-white);
    stroke-width: 1;
  }
</style>
</head>
<body>
<main class="poster" role="img" aria-label="Film title Orvela set in white over a sapphire to teal gradient">
  <svg class="poster__art" viewBox="0 0 826 1200" xmlns="http://www.w3.org/2000/svg">
    <g class="title-block">
      <text class="title-letter" x="218" y="365">O</text>
      <text class="title-letter" x="604" y="365" text-anchor="end">R</text>
      <text class="title-letter" x="218" y="616">V</text>
      <text class="title-letter" x="604" y="616" text-anchor="end">E</text>
      <text class="title-letter" x="224" y="878">L</text>
      <text class="title-letter" x="604" y="878" text-anchor="end">A</text>
    </g>

    <g class="tagline-block">
      <text class="tagline" x="416" y="930" text-anchor="middle">THE LIGHT IN THE TONES</text>
      <line class="tagline-rule" x1="240" y1="945" x2="593" y2="945"/>
    </g>
  </svg>
</main>
</body>
</html>
```